Zielgruppe
Steuerberatung
Aufgabenstellung
Ich benötige eine Neuerstellung für ein vorhandenes Briefpapier. Bedeutet, eigentlich soll der aktuelle Inhalt neu erstellt werden, da mir die Rohdaten nicht mehr zur Verfügung stehen. Das aktuelle Briefpapier steht als .doc zur Verfügung. Ziel 1:1 Abbildung. Zudem muss die Adresse geändert werden.

```html
<!DOCTYPE html>
<html lang="de">
<head>
<meta charset="utf-8">
<title>Briefpapier – Markus Behrendt Steuerberater</title>
<link href="https://fonts.googleapis.com/css2?family=Arimo:wght@400;700&display=swap" rel="stylesheet">
<style>
  :root {
    --backdrop: #e4e4e6;
    --paper: #ffffff;
    --ink: #2b2b2b;
    --ink-soft: #555555;
    --brand: #4a4a4a;
    --rule: #9a9a9a;
    --watermark: #e2e2e2;
    --signature-tint: #e6e9f4;
  }
  * { margin: 0; padding: 0; box-sizing: border-box; }
  html, body {
    width: 1200px; height: 1010px; overflow: hidden;
    background: var(--backdrop);
    font-family: "Arimo", Arial, sans-serif;
    color: var(--ink);
  }
  .sheet {
    position: absolute; left: 257px; top: 20px;
    width: 686px; height: 970px;
    background: var(--paper);
    box-shadow: 0 2px 10px rgba(0,0,0,.12);
    overflow: hidden;
  }
  .brand {
    position: absolute; left: 440px; top: 46px;
    display: flex; align-items: center; gap: 12px;
    color: var(--brand);
  }
  .brand-dot { width: 34px; height: 34px; border-radius: 50%; background: var(--brand); }
  .brand-name { font-size: 19px; font-weight: 700; line-height: 1.05; }
  .brand-name span { display: block; font-size: 19px; }
  .contact {
    position: absolute; left: 455px; top: 112px;
    padding-left: 12px; border-left: 1px solid var(--rule);
    font-size: 8.5px; line-height: 1.35; color: var(--ink-soft);
  }
  .contact strong { color: var(--ink); }
  .contact ul { list-style: none; margin-top: 8px; }
  .contact li { display: flex; align-items: center; gap: 6px; }
  .contact svg { width: 8px; height: 8px; fill: var(--ink-soft); }
  .sender-line {
    position: absolute; left: 80px; top: 168px;
    font-size: 6.5px; color: var(--ink-soft);
  }
  .date { position: absolute; right: 80px; top: 238px; font-size: 12px; }
  .fold-mark {
    position: absolute; left: 22px; width: 16px; border-top: 1px solid var(--rule);
  }
  .fold-mark.upper { top: 343px; }
  .fold-mark.lower { top: 687px; }
  .letter {
    position: absolute; left: 80px; top: 300px; width: 540px;
    font-size: 12.5px; line-height: 1.4;
  }
  .subject { margin-bottom: 10px; }
  .salutation { margin-bottom: 12px; }
  .letter p.body { margin-bottom: 16px; }
  .closing { margin-top: 8px; font-size: 11px; }
  .signature {
    width: 170px; height: 46px; margin: 8px 0 6px 8px;
    background: var(--signature-tint); border-radius: 4px;
  }
  .signer { margin-left: 40px; font-size: 12px; }
  .watermark {
    position: absolute; right: -90px; bottom: 110px;
    width: 300px; height: 300px; border-radius: 50%;
    background: var(--watermark); opacity: .75;
  }
  .footer {
    position: absolute; left: 80px; right: 40px; bottom: 36px;
    display: flex; gap: 18px; align-items: flex-end;
    font-size: 8.5px; line-height: 1.35; color: var(--ink-soft);
  }
  .footer-col { padding-right: 18px; border-right: 1px solid var(--rule); }
  .footer-col:last-child { border-right: 0; padding-right: 0; }
</style>
</head>
<body>
<main class="sheet">
  <div class="watermark" aria-hidden="true"></div>

  <header class="brand">
    <div class="brand-dot"></div>
    <div class="brand-name">Markus Behrendt<span>Steuerberater</span></div>
  </header>

  <address class="contact">
    <strong>Markus Behrendt</strong> | Steuerberater<br>
    Lindenallee 112<br>
    30159 Hannover
    <ul>
      <li><svg viewBox="0 0 10 10"><path d="M2 0.5 4 2.5 3 4a6 6 0 0 0 3 3l1.5-1 2 2-1.5 1.5C4 9.5 .5 6 .5 2z"/></svg>+49 (0) 170 - 52 84 316</li>
      <li><svg viewBox="0 0 10 10"><path d="M2 0h5v3H2zM0 3.5h10v4.5H8V6H2v2H0zM2.5 7h5v3h-5z"/></svg>+49 (0) 511 - 62 19 07 45</li>
      <li><svg viewBox="0 0 10 10"><path d="M0 1.5h10v7H0zM.8 2.3 5 5.5l4.2-3.2"/></svg>info@kanzlei-behrendt.de</li>
      <li><svg viewBox="0 0 10 10"><circle cx="5" cy="5" r="4.5"/></svg>www.kanzlei-behrendt.de</li>
    </ul>
  </address>

  <p class="sender-line">Markus Behrendt | Lindenallee 112 | 30159 Hannover</p>
  <p class="date">12.03.2021</p>

  <div class="fold-mark upper"></div>
  <div class="fold-mark lower"></div>

  <section class="letter">
    <p class="subject">Betreffzeile</p>
    <p class="salutation">Sehr geehrte Damen und Herren,</p>
    <p class="body">In sollicitudin, metus et posuere blandit, erat dui bibendum eros, id vestibulum sem justo vel mauris. Ut tempor dolor ut justo vulputate, eu blandit libero faucibus. In laoreet, massa non ultricies tempor, est enim auctor mi, sit amet venenatis massa augue in justo. Praesent eu tincidunt diam. Maecenas id mi efficitur tellus interdum consectetur vel sed ante. Sed suscipit quis eros a fermentum. Curabitur ornare sit amet leo eu semper. Vestibulum pretium mi eu nisi. gadde.</p>
    <p class="body">Sed nunc est, iaculis vel enim ut, fringilla commodo lorem. Pellentesque facilisis tempus lorem eget porttitor. Morbi accumsan, nulla accumsan mollis maximus, lectus diam venenatis odio, quis bibendum elit ex a arcu. Fusce turpis erat, euismod sit amet dolor eu, hendrerit rhoncus libero. Phasellus convallis, mi vel pharetra sollicitudin, nisi purus maximus est, nec lobortis dolor enim et augue. Vestibulum auctor mi sit amet leo auctor egestas. Pellentesque eget endrerit rhoncus dan.</p>
    <p class="closing">Mit freundlichen Grüßen</p>
    <div class="signature" role="img" aria-label="Handschriftliche Unterschrift von Markus Behrendt in blauer Tinte"></div>
    <p class="signer">Markus Behrendt</p>
  </section>

  <footer class="footer">
    <div class="footer-col">Zuständige Aufsichtsbehörde:<br>Steuerberaterkammer Niedersachsen<br>Körperschaft des öffentlichen Rechts</div>
    <div class="footer-col">Zuständiges Finanzamt:<br>Finanzamt Hannover-Mitte<br>Steuernummer: 25/118/30712</div>
    <div class="footer-col">Bankverbindung:<br>DE 47 2505 0180 0912 3384 56<br>BIC: HNVRDE2X</div>
  </footer>
</main>
</body>
</html>
```